Sales Flyer or Trifold for selling our Monthly Computer Service

I need a flyer designed for our new monthly computer maintenance service. We have been using this software package for 3 years for business customers with much success, but now we want to sell this to individual residential clients with the idea that we can keep their computer safe, running well, and less of a hassle for them. It also will create a steady work load for my technicians, and stable recurring income.

I tried making something, but it is too amateur looking. The final design should look professional, be engaging, and draw from our existing web design, logos, business cards and such. Most importantly, it should make them see value in spending $29 per month to be part of the program. I will upload as much examples of other branding as I can to give you something to go off of. We try to use open sans for text. You should also visit brightowlsupport.example for our current design scheme. I anticipate that we may go through a few revisions on this, and that I will probably have other similar signage created with complimentary designs later.

Target Market(s)

My target market is local affluent residential customers in the middle aged and up age range. People who may be or have been used to having tech support at their office.

Industry/Entity Type

Computer Repair

Font styles to use
Sans Serif

Requirements
Must have
• mention the components of the service that we offer. my existing flyer shows all of those. we also must use the logo in some way. It should have our contact information on the flyer too.
Nice to have
• I'm not sure yet, I really can't picture what I want. I am thinking a trifold. Maybe a single pager...
Should not have
• Please, please, no people with headsets on in a call center, no horrible stock imagery. We are trying to show that we are NOT a faceless call center, but instead give off a feeling of personalized support. We want to be their tech guy. Also, please do not use words with negative connotations like 'service plan' or similar. There are a lot of scammers out there claiming to do something similar and we need to disassociate ourselves as much as we can from them.

```html
<!DOCTYPE html>
<html lang="en">
<head>
<meta charset="utf-8">
<title>Watchpost Flyer – Front and Back</title>
<link rel="stylesheet" href="https://fonts.googleapis.com/css2?family=Anton&family=Barlow+Condensed:ital,wght@0,400;0,500;0,600;0,700;1,500&display=swap">
<style>
  :root {
    --red: #e3141e;
    --red-dark: #b30d15;
    --black: #0b0b0b;
    --ink: #1a1a1a;
    --grey-bg: #8d8d8d;
    --white: #ffffff;
    --tick: #5cc12e;
  }
  * { margin: 0; padding: 0; box-sizing: border-box; }
  html, body { width: 1200px; height: 848px; overflow: hidden; }
  body {
    background: var(--grey-bg);
    font-family: "Barlow Condensed", "Arial Narrow", sans-serif;
    color: var(--ink);
    position: relative;
  }
  .page {
    position: absolute;
    top: 46px;
    width: 516px;
    height: 728px;
    background: var(--white);
    overflow: hidden;
    box-shadow: 0 2px 10px rgba(0,0,0,.35);
  }
  .page--front { left: 42px; }
  .page--back { left: 625px; }
  .page svg.backdrop { position: absolute; inset: 0; }
  .abs { position: absolute; }

  /* front */
  .brand-dot {
    left: 218px; top: 18px; width: 80px; height: 80px;
    border-radius: 50%; background: var(--red);
    box-shadow: 0 3px 8px rgba(0,0,0,.5);
  }
  .product-name {
    left: 0; right: 0; top: 104px; text-align: center;
    font-family: "Anton", "Arial Narrow", sans-serif;
    font-size: 74px; line-height: 1; letter-spacing: 1px;
    color: var(--red);
  }
  .product-tagline {
    left: 0; right: 0; top: 190px; text-align: center;
    font-weight: 600; font-size: 15.5px; letter-spacing: 1.6px;
    color: var(--white); text-transform: uppercase;
  }
  .hero-art {
    left: 22px; top: 238px; width: 472px; height: 140px;
    border-radius: 8px;
    background: radial-gradient(ellipse at center, #e83a40 0%, #c9c9c9 45%, #e9e9e9 80%);
  }
  .front-headline {
    left: 0; right: 0; top: 392px; text-align: center;
    font-weight: 600; font-size: 27px; line-height: 32px;
  }
  .front-headline .accent { color: var(--red); }
  .front-sub {
    left: 0; right: 0; top: 468px; text-align: center;
    font-style: italic; font-weight: 500; font-size: 20px; line-height: 21px;
  }
  .feature-list { left: 86px; top: 521px; width: 342px; list-style: none; }
  .feature-list li {
    height: 24px; margin-bottom: 7.2px; border-radius: 12px;
    background: linear-gradient(to bottom, var(--red) 0%, var(--red) 50%, var(--red-dark) 51%, var(--red) 100%);
    color: var(--white); text-align: center;
    font-size: 17px; line-height: 24px; font-weight: 500;
    box-shadow: 0 1px 2px rgba(0,0,0,.35);
  }

  /* back */
  .intro-panel {
    left: 30px; top: 21px; width: 465px; height: 81px;
    border: 2px solid #9a9a9a; border-radius: 10px 40px 40px 10px;
    background: linear-gradient(#1d1d1d, #050505);
  }
  .company-mark { left: 8px; top: 10px; width: 96px; text-align: center; }
  .company-mark .dot {
    width: 48px; height: 48px; border-radius: 50%;
    background: var(--red); margin: 0 auto 6px;
  }
  .company-mark .name {
    color: var(--white); font-size: 9.5px; font-weight: 600;
    letter-spacing: .4px; text-transform: uppercase;
  }
  .intro-text {
    left: 105px; top: 12px; width: 335px;
    color: var(--white); font-size: 11.5px; line-height: 14.2px;
  }
  .benefits { left: 33px; top: 119px; width: 455px; list-style: none; }
  .benefits li {
    position: relative; padding-left: 29px; margin-bottom: 14px;
    color: var(--white); font-size: 12px; line-height: 14.5px;
  }
  .benefits li:last-child { margin-bottom: 0; }
  .benefits li::before {
    content: ""; position: absolute; left: 0; top: 6px;
    width: 17px; height: 17px; border-radius: 50%; background: var(--tick);
  }
  .benefits li::after {
    content: ""; position: absolute; left: 6px; top: 8px;
    width: 5px; height: 9px; border: solid var(--white);
    border-width: 0 2px 2px 0; transform: rotate(45deg);
  }
  .extra-note {
    left: 38px; top: 442px; width: 282px;
    color: var(--white); font-style: italic; font-weight: 500;
    font-size: 14px; line-height: 18.2px;
  }
  .devices-art {
    left: 322px; top: 420px; width: 194px; height: 172px;
    background: linear-gradient(160deg, #f2f2f2 0%, #b5b5b5 55%, #6b6b6b 100%);
    clip-path: polygon(18% 30%, 100% 0, 100% 100%, 0 100%);
  }
  .phone-icon { left: 31px; top: 558px; }
  .call-label {
    left: 95px; top: 562px; font-weight: 700; font-size: 29px; line-height: 1;
    color: var(--black);
  }
  .call-number {
    left: 95px; top: 588px; font-weight: 700; font-size: 44px; line-height: 1;
    color: var(--red); letter-spacing: -.5px;
  }
  .call-hours { left: 97px; top: 631px; font-size: 12px; }
  .contact-col { top: 653px; font-size: 12px; line-height: 15.5px; }
  .contact-col .label { color: var(--red); }
  .contact-col .small { font-size: 8px; line-height: 10px; }
  .contact-col--address { left: 31px; }
  .contact-col--online { left: 188px; }
  .delivery-note {
    left: 330px; top: 637px; width: 178px; padding-left: 8px;
    border-left: 2px solid var(--red);
    font-size: 7.6px; line-height: 10.8px;
  }
</style>
</head>
<body>

<section class="page page--front" aria-label="Flyer front">
  <svg class="backdrop" width="516" height="728" viewBox="0 0 516 728">
    <path d="M0 0H516V290C430 210 300 200 258 202C200 204 90 214 0 290Z" fill="#0b0b0b"/>
    <path d="M0 290C90 214 200 204 258 202C300 200 430 210 516 290V300C430 222 300 212 258 214C200 216 90 226 0 300Z" fill="#e3141e"/>
    <path d="M0 300C90 226 200 216 258 214C300 212 430 222 516 300V306C430 228 300 218 258 220C200 222 90 232 0 306Z" fill="#bdbdbd"/>
    <rect x="10" y="10" width="496" height="260" rx="10" fill="none" stroke="#2b2b2b" stroke-width="1.5"/>
  </svg>
  <div class="abs brand-dot"></div>
  <div class="abs product-name">WATCHPOST</div>
  <div class="abs product-tagline">Computer protection and security for your home</div>
  <div class="abs hero-art" role="img" aria-label="Illustration of a laptop showing a red circuit screen, surrounded by gears, magnifying glasses, lightning bolts and tools"></div>
  <div class="abs front-headline">Tired of Worrying About Your Computer ?<br>Ask us About our <span class="accent">Watchpost</span> Service !</div>
  <div class="abs front-sub">A Complete Solution to keep your Computer<br>and Precious Files Safe and Protected</div>
  <ul class="abs feature-list">
    <li>Commercial Grade Antivirus &amp; Antispyware</li>
    <li>Online and Local File Backup</li>
    <li>Malicious Website Filtering</li>
    <li>Automatic Update Installation</li>
    <li>Hardware and Software Trouble Monitoring</li>
    <li>Priority Service with 20% off Labor Rates</li>
  </ul>
</section>

<section class="page page--back" aria-label="Flyer back">
  <svg class="backdrop" width="516" height="728" viewBox="0 0 516 728">
    <rect width="516" height="728" fill="#ffffff"/>
    <path d="M0 0H516V330C420 400 200 440 0 388Z" fill="#0b0b0b"/>
    <path d="M0 398C200 450 420 412 516 342V470C300 530 120 545 0 528Z" fill="#e3141e"/>
    <path d="M0 528C120 545 300 530 516 470V492C300 548 120 562 0 550Z" fill="#0b0b0b"/>
  </svg>

  <div class="abs intro-panel">
    <div class="abs company-mark">
      <div class="dot"></div>
      <div class="name">Bright Owl Support</div>
    </div>
    <p class="abs intro-text">At Bright Owl Support, we have years of experience protecting the computers and networks of our commercial business clients. Now, we are making the same Enterprise Grade security and protection available to our home users for a flat monthly rate. It's like having your own personal IT department!</p>
  </div>

  <ul class="abs benefits">
    <li>Centrally managed and monitored antivirus &amp; antimalware to stop malicious zero-day threats before they have a chance to infect your computer.</li>
    <li>Centrally monitored online backups of your files, folders, or even the whole operating system to protect precious data that could be damaged by viruses, fire, theft, or other disasters.</li>
    <li>Centrally managed web filtering customizable to 4 different levels of protection to keep your family safe.</li>
    <li>Automatic update and patch installation for Vantix OS as well as 3rd party software and plugins such as Brewline, Glint, and many others to close security holes and eliminate the guesswork of which updates to install.</li>
    <li>24x7x365 monitoring of critical Vantix OS services and hardware health, designed to alert you to problems BEFORE they happen.</li>
    <li>Automated maintenance cleaning of your computer to keep it running smooth.</li>
    <li>Discounted rates for on site or remote service calls for Watchpost clients.</li>
  </ul>

  <p class="abs extra-note">…and Watchpost is more than just a collection of software. We also include a personalized one-on-one tutoring session to teach you how to safely navigate the internet and use your computer.</p>

  <div class="abs devices-art" role="img" aria-label="Illustration of desktop computers, monitors, a laptop and a phone connected by thin lines"></div>

  <svg class="abs phone-icon" width="52" height="80" viewBox="0 0 52 80" aria-hidden="true">
    <rect x="0" y="0" width="52" height="80" rx="5" fill="#e3141e"/>
    <rect x="4" y="9" width="44" height="58" fill="#0b0b0b"/>
    <rect x="19" y="3.5" width="14" height="2" rx="1" fill="#0b0b0b"/>
    <circle cx="26" cy="73.5" r="3.5" fill="#ffffff"/>
  </svg>
  <div class="abs call-label">CALL US</div>
  <div class="abs call-number">555-014-2368</div>
  <div class="abs call-hours">Monday - Friday from 8:00am - 6:00pm</div>

  <div class="abs contact-col contact-col--address">
    <div class="label">Street Address</div>
    <div>1820 Orchard Ln.</div>
    <div>Maple Grove, IA 50999</div>
    <div class="small">(On-Site Service Area)</div>
  </div>
  <div class="abs contact-col contact-col--online">
    <div class="label">Email</div>
    <div>info@brightowlsupport.example</div>
    <div class="label">Website</div>
    <div>www.brightowlsupport.example</div>
  </div>

  <p class="abs delivery-note">Free pickup and delivery applies to an area within 5 miles of our address.<br>An additional fee of $10 per trip will be charged if outside of this area for each visit.<br>If you would like to ship your computer or hard drive to us for work, please contact us first to make arrangements.</p>
</section>

</body>
</html>
```